Business Card Design

We need a business card for a well established Semi Trailer Hire company. I am looking for a new start as we are moving so would like to update our Business Cards and Letter heads.
We hire Semi Trailers to Transport companies.
The colour of our Trailers are Cherry Red so this must be the prominent colour.
I do not want any pictures of trailers on the design.
I do not want the design to be flowery in anyway as we are in the transport industry.
Simple yet effective

Brenlow Hire Pty Ltd
Ros Dunmore
Director
Ph: 03 9412 5083
Mobile: 0421 736 209
ros.dunmore@brenlowhire.com.au
www.brenlowhire.com.au
214-220 Pellow Road, Yarraville

```html
<!DOCTYPE html>
<html lang="en">
<head>
<meta charset="utf-8">
<title>Brenlow Hire Pty Ltd — Business Card</title>
<link rel="stylesheet" href="https://fonts.googleapis.com/css2?family=EB+Garamond:wght@400;500&family=Quicksand:wght@500&display=swap">
<style>
  :root {
    --cherry: #b01e24;
    --paper: #ffffff;
    --ink: #111111;
    --backdrop: #e9e9e9;
  }
  * { margin: 0; padding: 0; box-sizing: border-box; }
  html, body { width: 1100px; height: 1200px; overflow: hidden; }
  body {
    background: var(--backdrop);
    position: relative;
    font-family: "EB Garamond", serif;
  }
  .card {
    position: absolute;
    left: 100px;
    width: 900px;
    height: 530px;
    background: var(--paper);
    box-shadow: 0 6px 18px rgba(0,0,0,0.18);
    overflow: hidden;
  }
  .card-back { top: 45px; }
  .card-front { top: 625px; }

  /* Back */
  .back-bar {
    position: absolute;
    left: 0; top: 425px;
    width: 317px; height: 20px;
    background: var(--cherry);
  }
  .back-company {
    position: absolute;
    left: 357px; top: 408px;
    font-size: 42px;
    line-height: 50px;
    color: var(--cherry);
    letter-spacing: 0.5px;
    white-space: nowrap;
  }

  /* Front */
  .front-art { position: absolute; inset: 0; }
  .holder {
    position: absolute;
    left: 0; top: 205px;
    width: 380px;
    text-align: center;
    color: var(--paper);
  }
  .holder-name { font-size: 52px; line-height: 60px; letter-spacing: 1px; }
  .holder-role { font-size: 38px; line-height: 46px; letter-spacing: 1.5px; }

  .company {
    position: absolute;
    left: 432px; top: 62px;
    width: 436px;
  }
  .company-name {
    font-size: 32px;
    line-height: 38px;
    color: var(--cherry);
    white-space: nowrap;
    padding-bottom: 2px;
    border-bottom: 3px solid var(--ink);
  }
  .company-address {
    font-family: "Quicksand", sans-serif;
    font-size: 18px;
    line-height: 28px;
    color: var(--cherry);
    padding-left: 19px;
    letter-spacing: 0.5px;
    white-space: nowrap;
  }

  .contacts {
    position: absolute;
    left: 466px; top: 312px;
    list-style: none;
    font-family: "Quicksand", sans-serif;
    font-size: 18px;
    color: var(--cherry);
  }
  .contacts li {
    display: flex;
    align-items: center;
    height: 38px;
    white-space: nowrap;
  }
  .contacts svg { width: 20px; height: 20px; margin-right: 25px; flex: none; }
</style>
</head>
<body>

<section class="card card-back" aria-label="Card back">
  <div class="back-bar"></div>
  <div class="back-company">BRENLOW HIRE PTY LTD</div>
</section>

<section class="card card-front" aria-label="Card front">
  <svg class="front-art" viewBox="0 0 900 530" width="900" height="530" aria-hidden="true">
    <path d="M0 0 H380 C405 160 385 390 276 530 H0 Z" fill="var(--cherry)"/>
    <path d="M380 0 C405 160 385 390 276 530" fill="none" stroke="var(--ink)" stroke-width="4"/>
  </svg>

  <div class="holder">
    <div class="holder-name">Ros Dunmore</div>
    <div class="holder-role">Director</div>
  </div>

  <div class="company">
    <div class="company-name">BRENLOW HIRE PTY LTD</div>
    <div class="company-address">214-220 Pellow Road, Yarraville</div>
  </div>

  <ul class="contacts">
    <li>
      <svg viewBox="0 0 24 24" aria-hidden="true"><g fill="none" stroke="var(--cherry)" stroke-width="1.8"><circle cx="12" cy="12" r="9"/><ellipse cx="12" cy="12" rx="4" ry="9"/><path d="M3 12h18M5 7h14M5 17h14"/></g></svg>
      WWW.BRENLOWHIRE.COM.AU
    </li>
    <li>
      <svg viewBox="0 0 24 24" aria-hidden="true"><rect x="2" y="5" width="20" height="14" fill="var(--cherry)"/><path d="M2 5l10 8 10-8" fill="none" stroke="#fff" stroke-width="1.6"/></svg>
      ROS.DUNMORE@BRENLOWHIRE.COM.AU
    </li>
    <li>
      <svg viewBox="0 0 24 24" aria-hidden="true"><path d="M2 9c0-3 4-4 10-4s10 1 10 4v1h-5V8H7v2H2z M6 11h12l3 9H3z" fill="var(--cherry)"/><circle cx="12" cy="15" r="2.5" fill="#fff"/></svg>
      03 9412 5083
    </li>
    <li>
      <svg viewBox="0 0 24 24" aria-hidden="true"><rect x="6.5" y="2" width="11" height="20" rx="2" fill="none" stroke="var(--cherry)" stroke-width="2"/><circle cx="12" cy="18.5" r="1.2" fill="var(--cherry)"/></svg>
      0421 736 209
    </li>
  </ul>
</section>

</body>
</html>
```